IT Consulting company Needs a Logo Design and Business Cards

I need a New Logo and Business Cards for an established IT Managed Services Company that specializes in flat-rate managed IT services. We provide Design and Build, Help Desk, Onsite and Remote Support Services.

Target Market(s)

Corporate Clients

Industry/Entity Type

It Company

Logo Text

Halbrook Computer Group

Requirements
Nice to have
• Tag Line= Technology at Lightning Speed

```html
<!DOCTYPE html>
<html lang="en">
<head>
<meta charset="UTF-8">
<title>Halbrook Computer Group – Business Cards</title>
<link href="https://fonts.googleapis.com/css2?family=Arimo:wght@400;700&display=swap" rel="stylesheet">
<style>
  :root {
    --brand-blue: #239cd9;
    --paper: #ffffff;
    --ink: #555b61;
    --backdrop: #e9ebee;
    --rule: #6bb8e4;
  }
  * { box-sizing: border-box; margin: 0; padding: 0; }
  html, body {
    width: 1200px; height: 800px; overflow: hidden;
    background: var(--backdrop);
  }
  .sheet {
    width: 1200px; height: 800px;
    display: flex; align-items: center; justify-content: center; gap: 40px;
  }
  .card {
    position: relative;
    width: 540px; height: 310px;
    overflow: hidden;
    box-shadow: 0 6px 18px rgba(0,0,0,0.12);
    font-family: "Arimo", sans-serif;
  }

  /* Front */
  .card--front { background: var(--brand-blue); }
  .card--front .bottom-band {
    position: absolute; left: 0; right: 0; bottom: 0; height: 46px;
    background: var(--paper);
  }
  .company-name {
    font-family: "Arimo", sans-serif;
    font-weight: 700;
    line-height: 1.15;
  }
  .card--front .company-name {
    position: absolute; left: 0; right: 0; top: 100px;
    text-align: center;
    font-size: 34px;
    color: var(--paper);
  }
  .tagline {
    position: absolute; left: 0; right: 0; bottom: 62px;
    text-align: center;
    font-size: 14px; letter-spacing: 3px; color: var(--paper);
  }

  /* Back */
  .card--back { background: var(--paper); }
  .card--back .company-name {
    position: absolute; left: 30px; top: 100px; width: 250px;
    font-size: 24px;
    color: var(--brand-blue);
  }

  .divider {
    position: absolute; left: 298px; top: 48px;
    width: 1px; height: 150px; background: var(--rule);
  }
  .contact {
    position: absolute; left: 318px; top: 56px;
    color: var(--ink);
  }
  .contact__name { font-size: 21px; font-weight: 700; color: var(--brand-blue); }
  .contact__role { font-size: 12px; margin-bottom: 12px; }
  .contact__line { font-size: 12px; line-height: 1.5; display: flex; align-items: center; gap: 5px; }
  .contact__line svg { width: 10px; height: 10px; fill: var(--brand-blue); flex: none; }

  .service-band {
    position: absolute; left: 0; right: 0; bottom: 14px; height: 40px;
    background: var(--brand-blue);
    display: flex; align-items: center; justify-content: center;
    font-size: 13.5px; letter-spacing: 2px;
    color: var(--paper);
  }
</style>
</head>
<body>
<main class="sheet">

  <section class="card card--front" aria-label="Business card front">
    <p class="company-name">Halbrook Computer Group</p>
    <p class="tagline">Technology at Lightning Speed</p>
    <div class="bottom-band"></div>
  </section>

  <section class="card card--back" aria-label="Business card back">
    <p class="company-name">Halbrook<br>Computer Group</p>

    <div class="divider"></div>

    <div class="contact">
      <p class="contact__name">Daniel Reeve</p>
      <p class="contact__role">Director</p>
      <p class="contact__line">PO Box 418, Carlow Lane</p>
      <p class="contact__line">2nd Street Eastvale</p>
      <p class="contact__line">
        <svg viewBox="0 0 10 10" aria-hidden="true"><path d="M2 0.5 L3.6 2.6 L2.6 3.6 Q3.8 6 6.4 7.4 L7.4 6.4 L9.5 8 L8.2 9.5 Q4.5 9.5 0.5 1.8 Z"/></svg>
        (555) 214 0387
      </p>
      <p class="contact__line">
        <svg viewBox="0 0 10 10" aria-hidden="true"><path d="M0.5 2 H9.5 V8.5 H0.5 Z M1.2 2.6 L5 5.6 L8.8 2.6" stroke="#fff" stroke-width="0.8"/></svg>
        info@halbrookgroup.com
      </p>
    </div>

    <div class="service-band">Build | Help Desk | Onsite | Remote Support Services</div>
  </section>

</main>
</body>
</html>
```